Redesign of SnapRoute Windows Phone app

The App exists, is up and running but the design is not the best (my creation and i am a developer).
Project landing page http://snaproute.example/

Also the app has live tiles small, medium and large.

The purpose of this is to have a professional design and make this app the best app on the Windows Phone marketplace of his kind.

This app is a picture library that tells you where you've made you're pictures and gives you a unique perspective on the places that you have visited.

If this is successful there will be a version for Windows 8, Android and IOS also.

The app right now is for WP7 and WP8 and because of this the performance is not the best. With this new design the app will be for WP8 only and have the best performance possible.

I am not sure what else should i mention here but i am glad to answer to any questions if you are interested.

I am using Expression design as a design tool and Expression Blend and Visual studio as development tools so if you can provide compatible file the better but is not mandatory.

It wold be nice to keep the existing color palette but again nothing is mandatory I just need a good design.

Links:
App on Marketplace http://www.appmarket.example/en-us/store/app/snaproute/7f3a9d21-8b4c-4e6f-a1d2-93c7b5e08f14

App landing page http://snaproute.example/
Updates

We can do better, I will increase the budget with 200$  so the total budget will be 480$ so please consider this more seriously.

Thank you.

Target Market(s)

Windows Phone users that travel and make pictures.

Industry/Entity Type

Library

Requirements
Must have
• Panorama control as the App main page like in the present.

Representation of visited locations , Live tiles, Map, share location and picture..

If the designer comes up with better proposition they will be take in consideration.

None of these are mandatory but we should keep a connection with the present design so the users will not have the impression that this is a totally different app, this is SnapRoute but better, more professional.

```html
<!DOCTYPE html>
<html lang="en">
<head>
<meta charset="utf-8">
<title>SnapRoute – Panorama</title>
<link rel="stylesheet" href="https://fonts.googleapis.com/css2?family=Open+Sans:wght@300;400;600&display=swap">
<style>
:root{
  --cream:#fbf3e6;
  --white:#ffffff;
  --blue:#2a8bbf;
  --blue-light:#3a9fd6;
  --orange:#f7a11a;
  --magenta:#c8179b;
  --ink:#333333;
  --ink-soft:#666666;
  --skyline:#2b2b2b;
  --map:#e4e1d8;
}
*{box-sizing:border-box;margin:0;padding:0}
html,body{width:1200px;height:734px;overflow:hidden;background:var(--white)}
body{font-family:"Open Sans",Arial,sans-serif;color:var(--ink)}
.canvas{position:relative;width:1200px;height:734px;overflow:hidden;background:var(--white)}
.backdrop{position:absolute;inset:0}
.brand{position:absolute;left:56px;top:40px;display:flex;align-items:center;gap:10px}
.brand-dot{width:30px;height:30px;border-radius:50%;background:var(--magenta)}
.brand-name{font-size:33px;font-weight:400;color:var(--blue);letter-spacing:.2px}
.skyline{position:absolute;left:0;top:54px;width:933px;height:96px;
  background:linear-gradient(180deg,rgba(43,43,43,0) 0%,rgba(43,43,43,.25) 45%,var(--skyline) 80%,var(--skyline) 100%)}
.sky-pin{position:absolute}
.col-head{position:absolute;top:158px;height:57px;background:var(--blue);border-top-right-radius:30px;
  color:var(--white);display:flex;align-items:center;gap:12px;padding-left:18px;font-size:27px;font-weight:400}
.col-head svg{flex:none}
.map{position:absolute;left:63px;top:236px;width:272px;height:462px;background:linear-gradient(160deg,#ebe8df,#dcd8cc)}
.map-pin{position:absolute}
.share{position:absolute;left:180px;top:554px;width:136px;height:136px;border-radius:50%;
  background:rgba(255,255,255,.55);border:4px solid #c9c9c9}
.share-dot{position:absolute;width:34px;height:34px;border-radius:50%;background:var(--blue-light)}
.tile{position:absolute;width:231px;height:94px;overflow:hidden;background:var(--white)}
.tile-photo{position:absolute;left:64px;top:0;right:0;bottom:0;
  background:linear-gradient(180deg,#6fb3e6 0%,#a9d1ef 38%,#c9b59a 60%,#8f7a62 100%)}
.tile-badge{position:absolute;left:-86px;bottom:-86px;width:172px;height:172px;border-radius:50%}
.tile.location .tile-badge{background:var(--orange)}
.tile.album .tile-badge{background:var(--magenta)}
.tile-count{position:absolute;left:12px;bottom:12px;font-size:24px;font-weight:400;color:var(--ink)}
.tile.album .tile-count{color:var(--white)}
.tile.faded .tile-count{font-weight:300;opacity:.85}
.tile-city{position:absolute;left:95px;bottom:16px;font-size:20px;color:var(--white);font-weight:400}
.tile-street{position:absolute;right:6px;bottom:2px;font-size:11.5px;color:var(--white);letter-spacing:.3px}
.date-list{position:absolute;right:19px;top:242px;width:220px;text-align:right;list-style:none}
.date-item{height:80px}
.date-when{font-size:18px;color:var(--ink)}
.date-count{font-size:10px;color:var(--ink-soft);line-height:1.3}
.date-last{font-size:13px;color:var(--ink-soft)}
</style>
</head>
<body>
<main class="canvas">
  <svg class="backdrop" width="1200" height="734" viewBox="0 0 1200 734" aria-hidden="true">
    <polygon points="0,0 933,0 933,150 345,405 0,690" fill="var(--cream)"/>
  </svg>

  <header class="brand">
    <span class="brand-dot"></span>
    <span class="brand-name">SnapRoute</span>
  </header>

  <div class="skyline" role="img" aria-label="City skyline silhouette with clouds"></div>
  <svg class="sky-pin" style="left:341px;top:100px" width="26" height="36" viewBox="0 0 26 36" aria-hidden="true">
    <path d="M13 0C5.8 0 0 5.8 0 13c0 9.5 13 23 13 23s13-13.5 13-23C26 5.8 20.2 0 13 0z" fill="var(--orange)"/>
    <circle cx="13" cy="13" r="6" fill="var(--white)"/>
  </svg>
  <svg class="sky-pin" style="left:660px;top:86px" width="38" height="52" viewBox="0 0 26 36" aria-hidden="true">
    <path d="M13 0C5.8 0 0 5.8 0 13c0 9.5 13 23 13 23s13-13.5 13-23C26 5.8 20.2 0 13 0z" fill="var(--orange)"/>
    <circle cx="13" cy="13" r="6" fill="var(--white)"/>
  </svg>

  <!-- Map column -->
  <div class="col-head" style="left:62px;width:274px"></div>
  <section class="map" role="img" aria-label="Street map of the visited neighbourhood">
    <svg class="map-pin" style="left:182px;top:34px" width="34" height="48" viewBox="0 0 26 36" aria-hidden="true">
      <path d="M13 0C5.8 0 0 5.8 0 13c0 9.5 13 23 13 23s13-13.5 13-23C26 5.8 20.2 0 13 0z" fill="var(--magenta)"/>
      <circle cx="13" cy="13" r="6" fill="var(--white)"/>
    </svg>
    <svg class="map-pin" style="left:49px;top:82px" width="34" height="48" viewBox="0 0 26 36" aria-hidden="true">
      <path d="M13 0C5.8 0 0 5.8 0 13c0 9.5 13 23 13 23s13-13.5 13-23C26 5.8 20.2 0 13 0z" fill="var(--magenta)"/>
      <circle cx="13" cy="13" r="6" fill="var(--white)"/>
    </svg>
  </section>
  <div class="share">
    <span class="share-dot" style="left:46px;top:12px"></span>
    <span class="share-dot" style="left:8px;top:52px"></span>
    <span class="share-dot" style="left:86px;top:52px"></span>
    <svg style="position:absolute;left:50px;top:44px" width="30" height="42" viewBox="0 0 26 36" aria-hidden="true">
      <path d="M13 0C5.8 0 0 5.8 0 13c0 9.5 13 23 13 23s13-13.5 13-23C26 5.8 20.2 0 13 0z" fill="var(--magenta)"/>
      <circle cx="13" cy="13" r="6" fill="var(--white)"/>
    </svg>
  </div>

  <!-- Locations column -->
  <h2 class="col-head" style="left:393px;width:231px">
    <svg width="18" height="26" viewBox="0 0 26 36" aria-hidden="true">
      <path d="M13 0C5.8 0 0 5.8 0 13c0 9.5 13 23 13 23s13-13.5 13-23C26 5.8 20.2 0 13 0z" fill="var(--white)"/>
      <circle cx="13" cy="13" r="5" fill="var(--blue)"/>
    </svg>
    <span>locations</span>
    <svg width="18" height="14" viewBox="0 0 18 14" aria-hidden="true" fill="var(--white)">
      <rect x="0" y="0" width="4" height="3"/><rect x="6" y="0" width="12" height="3"/>
      <rect x="0" y="5.5" width="4" height="3"/><rect x="6" y="5.5" width="12" height="3"/>
      <rect x="0" y="11" width="4" height="3"/><rect x="6" y="11" width="12" height="3"/>
    </svg>
  </h2>
  <article class="tile location" style="left:393px;top:243px">
    <div class="tile-photo" role="img" aria-label="Photo of a stone monument under blue sky"></div>
    <div class="tile-badge"></div><span class="tile-count">26</span>
    <span class="tile-city">Rome</span><span class="tile-street">Fenwick Lane no 5</span>
  </article>
  <article class="tile location" style="left:393px;top:364px">
    <div class="tile-photo" role="img" aria-label="Photo of a stone monument under blue sky"></div>
    <div class="tile-badge"></div><span class="tile-count">125</span>
    <span class="tile-city">Rome</span><span class="tile-street">Fenwick Lane no 5</span>
  </article>
  <article class="tile location" style="left:393px;top:486px">
    <div class="tile-photo" role="img" aria-label="Photo of a stone monument under blue sky"></div>
    <div class="tile-badge"></div><span class="tile-count">48</span>
    <span class="tile-city">Rome</span><span class="tile-street">Fenwick Lane no 5</span>
  </article>
  <article class="tile location faded" style="left:393px;top:607px">
    <div class="tile-photo" role="img" aria-label="Photo of a stone monument under blue sky"></div>
    <div class="tile-badge"></div><span class="tile-count">48</span>
    <span class="tile-city">Rome</span><span class="tile-street">Fenwick Lane no 5</span>
  </article>

  <!-- Albums column -->
  <h2 class="col-head" style="left:680px;width:234px">
    <svg width="24" height="22" viewBox="0 0 24 22" aria-hidden="true">
      <rect x="1.5" y="1.5" width="21" height="19" fill="none" stroke="var(--white)" stroke-width="2.5"/>
      <polygon points="4,18 10,10 14,15 17,12 20,18" fill="var(--white)"/>
      <circle cx="8" cy="7" r="2" fill="var(--white)"/>
    </svg>
    <span>albums</span>
    <svg width="18" height="14" viewBox="0 0 18 14" aria-hidden="true" fill="var(--white)">
      <rect x="0" y="0" width="4" height="3"/><rect x="6" y="0" width="12" height="3"/>
      <rect x="0" y="5.5" width="4" height="3"/><rect x="6" y="5.5" width="12" height="3"/>
      <rect x="0" y="11" width="4" height="3"/><rect x="6" y="11" width="12" height="3"/>
    </svg>
  </h2>
  <article class="tile album" style="left:680px;top:243px">
    <div class="tile-photo" role="img" aria-label="Album cover photo of a stone monument"></div>
    <div class="tile-badge"></div><span class="tile-count">26</span>
    <span class="tile-city">Rome</span><span class="tile-street">Fenwick Lane no 5</span>
  </article>
  <article class="tile album" style="left:680px;top:364px">
    <div class="tile-photo" role="img" aria-label="Album cover photo of a stone monument"></div>
    <div class="tile-badge"></div><span class="tile-count">125</span>
    <span class="tile-city">Rome</span><span class="tile-street">Fenwick Lane no 5</span>
  </article>
  <article class="tile album" style="left:680px;top:486px">
    <div class="tile-photo" role="img" aria-label="Album cover photo of a stone monument"></div>
    <div class="tile-badge"></div><span class="tile-count">48</span>
    <span class="tile-city">Rome</span><span class="tile-street">Fenwick Lane no 5</span>
  </article>
  <article class="tile album faded" style="left:680px;top:607px">
    <div class="tile-photo" role="img" aria-label="Album cover photo of a stone monument"></div>
    <div class="tile-badge"></div><span class="tile-count">48</span>
    <span class="tile-city">Rome</span><span class="tile-street">Fenwick Lane no 5</span>
  </article>

  <!-- Dates column -->
  <h2 class="col-head" style="left:968px;width:232px;border-top-right-radius:0;padding-left:56px">
    <svg width="24" height="24" viewBox="0 0 24 24" aria-hidden="true" fill="var(--white)">
      <rect x="1" y="3" width="22" height="20" fill="none" stroke="var(--white)" stroke-width="2"/>
      <rect x="1" y="3" width="22" height="5"/>
      <rect x="5" y="0" width="2.5" height="5"/><rect x="16.5" y="0" width="2.5" height="5"/>
      <rect x="5" y="11" width="3" height="3"/><rect x="10.5" y="11" width="3" height="3"/><rect x="16" y="11" width="3" height="3"/>
      <rect x="5" y="16.5" width="3" height="3"/><rect x="10.5" y="16.5" width="3" height="3"/><rect x="16" y="16.5" width="3" height="3"/>
    </svg>
    <span>dates</span>
  </h2>
  <ul class="date-list">
    <li class="date-item"><p class="date-when">2 minutes ago</p><p class="date-count">3 pictures</p><p class="date-last">Last date: 02.08.2013 13:00</p></li>
    <li class="date-item"><p class="date-when">2 minutes ago</p><p class="date-count">3 pictures</p><p class="date-last">Last date: 02.08.2013 13:00</p></li>
    <li class="date-item"><p class="date-when">2 minutes ago</p><p class="date-count">3 pictures</p><p class="date-last">Last date: 02.08.2013 13:00</p></li>
    <li class="date-item"><p class="date-when">2 minutes ago</p><p class="date-count">3 pictures</p><p class="date-last">Last date: 02.08.2013 13:00</p></li>
    <li class="date-item"><p class="date-when">2 minutes ago</p><p class="date-count">3 pictures</p><p class="date-last">Last date: 02.08.2013 13:00</p></li>
    <li class="date-item"><p class="date-when">2 minutes ago</p><p class="date-count">3 pictures</p><p class="date-last">Last date: 02.08.2013 13:00</p></li>
  </ul>
</main>
</body>
</html>
```